Classy, Elegant, Simple Business Card Design

Looking to have a classy, simple, and elegant design. Want a top notch designed business card. I really like the look of the new veltro credit card. I also like the design I attached. I am trying to reach 21-29 year old females for booking us for there wedding or event. We offer Disc Jockey Service, Photo Booth Rentals, and Uplighting .

Target Market(s)

21-28 year old females

Contact Information for Business Card

Has to have logo, website, email, and phone number

Font styles to use
Other font styles liked:
• open to font choice, modern, clean
Designer to choose
33a6d7
0791cd
0555a3
ffffff

Requirements
Must have
• Has to have logo, website, email, and phone number
Nice to have
• I really like the design of the new veltro credit card. I also included my logo and some designs I like
Should not have
• clutter or too much info

```html
<!DOCTYPE html>
<html lang="en">
<head>
<meta charset="UTF-8">
<title>Tidecrest Event Group – Business Card</title>
<link href="https://fonts.googleapis.com/css2?family=Roboto:wght@300;400;500&display=swap" rel="stylesheet">
<style>
  :root {
    --backdrop: #3a3a3c;
    --card: #1c1c1e;
    --ink: #ffffff;
    --ink-soft: #d9d9d9;
    --sky: #33a6d7;
    --azure: #0791cd;
    --deep: #0555a3;
    --divider: #4a4a4e;
  }
  * { margin: 0; padding: 0; box-sizing: border-box; }
  html, body { width: 799px; height: 1200px; overflow: hidden; }
  body {
    background: var(--backdrop);
    font-family: "Roboto", sans-serif;
    color: var(--ink);
    display: flex;
    flex-direction: column;
    align-items: center;
    justify-content: space-around;
    padding: 60px 0;
  }
  .card {
    width: 630px;
    height: 360px;
    background: var(--card);
    border-radius: 6px;
    box-shadow: 0 18px 40px rgba(0,0,0,0.45);
    position: relative;
  }
  /* Front */
  .card--front {
    display: flex;
    flex-direction: column;
    align-items: center;
    justify-content: center;
  }
  .brand-name {
    font-weight: 400;
    font-size: 44px;
    letter-spacing: 3px;
    color: var(--ink-soft);
    text-transform: uppercase;
    text-align: center;
    line-height: 1.15;
  }
  .services {
    margin-top: 48px;
    font-size: 19px;
    font-weight: 400;
    color: var(--ink);
    display: flex;
    gap: 16px;
  }
  .services .sep { color: var(--azure); }
  /* Back */
  .card--back {
    display: flex;
    align-items: center;
    padding: 0 40px;
  }
  .back-brand {
    width: 260px;
    font-size: 30px;
    font-weight: 400;
    letter-spacing: 2px;
    text-transform: uppercase;
    color: var(--azure);
    line-height: 1.2;
    text-align: center;
  }
  .back-divider {
    width: 0;
    height: 170px;
    border-left: 2px dotted var(--divider);
    margin: 0 32px;
  }
  .contact-title {
    font-size: 25px;
    font-weight: 400;
    color: var(--sky);
  }
  .contact-subtitle {
    font-size: 15px;
    color: var(--ink);
    margin-top: 4px;
    margin-bottom: 22px;
  }
  .contact-list { list-style: none; }
  .contact-list li {
    display: flex;
    align-items: center;
    gap: 10px;
    font-size: 15px;
    line-height: 1.6;
  }
  .contact-list svg { width: 14px; height: 14px; fill: var(--azure); flex: none; }
</style>
</head>
<body>
  <section class="card card--front">
    <h1 class="brand-name">Tidecrest<br>Event Group</h1>
    <p class="services">
      <span>Disc Jockeys</span><span class="sep">/</span>
      <span>Photo Booths</span><span class="sep">/</span>
      <span>And More..</span>
    </p>
  </section>

  <section class="card card--back">
    <div class="back-brand">Tidecrest<br>Event Group</div>
    <div class="back-divider"></div>
    <div class="contact">
      <h2 class="contact-title">Tidecrest Event Group</h2>
      <p class="contact-subtitle">Information &amp; Bookings</p>
      <ul class="contact-list">
        <li>
          <svg viewBox="0 0 24 24" aria-hidden="true"><path d="M6.6 10.8a15.1 15.1 0 0 0 6.6 6.6l2.2-2.2c.3-.3.7-.4 1-.2 1.1.4 2.3.6 3.6.6.6 0 1 .4 1 1V20c0 .6-.4 1-1 1A17 17 0 0 1 3 4c0-.6.4-1 1-1h3.5c.6 0 1 .4 1 1 0 1.3.2 2.5.6 3.6.1.3 0 .7-.2 1z"/></svg>
          <span>555-014-2290</span>
        </li>
        <li>
          <svg viewBox="0 0 24 24" aria-hidden="true"><path d="M2 5h20v14H2zm2 2v.4l8 5 8-5V7zm0 2.8V17h16V9.8l-8 5z"/></svg>
          <span>Info@TidecrestEventGroup.com</span>
        </li>
        <li>
          <svg viewBox="0 0 24 24" aria-hidden="true"><path d="M12 2a10 10 0 1 0 0 20 10 10 0 0 0 0-20zm6.9 6h-3a15 15 0 0 0-1.3-3.9A8 8 0 0 1 18.9 8zM12 4c.8 1.1 1.5 2.5 1.9 4h-3.8c.4-1.5 1.1-2.9 1.9-4zM4.3 14a8 8 0 0 1 0-4h3.4a16 16 0 0 0 0 4zm.8 2h3a15 15 0 0 0 1.3 3.9A8 8 0 0 1 5.1 16zm3-8h-3a8 8 0 0 1 4.3-3.9A15 15 0 0 0 8.1 8zM12 20c-.8-1.1-1.5-2.5-1.9-4h3.8c-.4 1.5-1.1 2.9-1.9 4zm2.3-6H9.7a14 14 0 0 1 0-4h4.6a14 14 0 0 1 0 4zm.3 5.9a15 15 0 0 0 1.3-3.9h3a8 8 0 0 1-4.3 3.9zm1.7-5.9a16 16 0 0 0 0-4h3.4a8 8 0 0 1 0 4z"/></svg>
          <span>TidecrestEventGroup.com</span>
        </li>
      </ul>
    </div>
  </section>
</body>
</html>
```